Lumo-Grid Business Card Design

We are an Managed IT Services provider, our main aim is to support business IT outsourcing, we provide these services: Network Services ,Technical Support , In House IT Services , Server Solutions , Anti-Spam , Online backup , Brellix Desk Suite ,Work from Home Solutions , IT Planning & Installation.

Target Market(s)

Information Technology

Industry/Entity Type

Business

Contact Information for Business Card

Lumo-Grid, Inc.12103 Sailboat WayCooper City, FL 33026Phone: 305-720-7162Email: support@lumo-grid.com

Font styles to use
Serif

Requirements
Must have
• a nice logo

```html
<!DOCTYPE html>
<html lang="en">
<head>
<meta charset="utf-8">
<title>Lumo-Grid, Inc. — Business Card</title>
<link rel="stylesheet" href="https://fonts.googleapis.com/css2?family=Montserrat:wght@400;500;700&display=swap">
<style>
  :root {
    --page-bg: #ffffff;
    --card-cyan: #4fd8ff;
    --card-white: #ffffff;
    --band-grey: #e3e3e3;
    --service-ink: #2b2b9e;
  }
  html, body {
    margin: 0;
    padding: 0;
    width: 1200px;
    height: 999px;
    overflow: hidden;
    background: var(--page-bg);
  }
  .canvas {
    position: relative;
    width: 1200px;
    height: 999px;
  }
  .business-card {
    position: absolute;
    left: 283px;
    top: 323px;
    width: 635px;
    height: 354px;
    background: var(--card-cyan);
    overflow: hidden;
    font-family: "Montserrat", Arial, sans-serif;
    color: var(--card-white);
  }
  .brand {
    position: absolute;
    left: 39px;
    top: 54px;
    display: flex;
    align-items: flex-end;
    gap: 14px;
  }
  .brand-square {
    width: 78px;
    height: 63px;
    border: 2px solid var(--card-white);
    box-sizing: border-box;
    display: block;
  }
  .brand-name {
    margin: 0 0 -1px;
    font-size: 36px;
    font-weight: 700;
    letter-spacing: -0.5px;
    line-height: 1;
    color: var(--card-white);
    white-space: nowrap;
  }
  .contact {
    position: absolute;
    left: 40px;
    top: 140px;
    margin: 0;
    font-style: normal;
    font-size: 15.5px;
    font-weight: 400;
    line-height: 22px;
    letter-spacing: 0.2px;
  }
  .services-band {
    position: absolute;
    left: 0;
    top: 256px;
    width: 100%;
    height: 66px;
    background: var(--band-grey);
    box-sizing: border-box;
    padding: 14px 0 0 37px;
  }
  .services-list {
    margin: 0;
    padding: 0;
    list-style: none;
    font-size: 13.6px;
    font-weight: 500;
    line-height: 17px;
    color: var(--service-ink);
    white-space: nowrap;
  }
</style>
</head>
<body>
<main class="canvas">
  <section class="business-card" aria-label="Lumo-Grid, Inc. business card">
    <header class="brand">
      <span class="brand-square" aria-hidden="true"></span>
      <h1 class="brand-name">Lumo-Grid, Inc.</h1>
    </header>

    <address class="contact">
      48217 Heron Crest Lane<br>
      Brisa Harbor, FL 33981<br>
      Phone: 305-418-9253<br>
      Email: support@lumo-grid.com
    </address>

    <div class="services-band">
      <ul class="services-list">
        <li>• Network Services • Technical Support • In House IT Services • Server Solutions</li>
        <li>• Anti-Spam • Online backup • Work from Home Solutions • IT Planning &amp; Installation</li>
      </ul>
    </div>
  </section>
</main>
</body>
</html>
```